Verlin Auto Repair - Flyer Design

My business is a automobile shop where we fix cars. Such things that we do but not limited to is brakes, Engine/Transmission change, Electrical work, emission test, oil change and automobile diagnostic. I am looking for a flyer that will catch peoples attention, I will be giving flyers to people, putting them in car windows and mailboxes. I am looking for a flier that will help to attract more customers to my business. I also want the flyer to say "Bring in your estimate from our competitors with this flyer and we will beat it by 10%" (does not have to be in those exact words). I also want the flyer to have my business address phone and operating hours. I have attached a business card and my business ad which I have placed in the newspaper before. I hope it helps with your design.
Industry/Entity Type
Car Repair
Look and feel
Each slider illustrates characteristics of the customer's brand and the style your logo design should communicate.

```html
<!DOCTYPE html>
<html lang="en">
<head>
<meta charset="utf-8">
<title>Verlin Auto Repair – Flyer</title>
<link rel="stylesheet" href="https://fonts.googleapis.com/css2?family=Ultra&family=Oswald:wght@400;500;600&family=Roboto+Condensed:wght@400;700&family=Anton&display=swap">
<style>
  :root {
    --ink: #1c1b1c;
    --paper: #ececec;
    --red: #d81820;
    --white: #f4f4f4;
    --stage: #e4e2df;
  }
  * { margin: 0; padding: 0; box-sizing: border-box; }
  html, body { width: 1200px; height: 1200px; overflow: hidden; background: var(--stage); }
  .flyer {
    position: absolute; left: 337px; top: 30px;
    width: 526px; height: 1140px;
    background: var(--paper);
    box-shadow: 0 6px 24px rgba(0,0,0,.25);
    overflow: hidden;
  }
  .hero { position: absolute; left: 0; top: 0; width: 100%; height: 420px; background: var(--ink); }
  .hero-photo {
    position: absolute; right: 0; top: 0; width: 270px; height: 420px;
    background: linear-gradient(160deg, #cfcfcf 0%, #6a6a6a 35%, #2a2a2a 70%, #1c1b1c 100%);
  }
  .brand {
    position: absolute; left: 30px; top: 150px; z-index: 1;
    font-family: "Ultra", serif; font-weight: 400; color: var(--white);
    font-size: 50px; line-height: 72px; letter-spacing: 1px;
  }
  .details { position: absolute; left: 0; top: 420px; width: 100%; height: 370px; padding: 30px 36px 0 48px; color: var(--ink); }
  .contact { list-style: none; font-family: "Roboto Condensed", sans-serif; font-weight: 700; font-size: 24px; line-height: 28px; }
  .contact li { display: flex; align-items: flex-start; gap: 12px; }
  .contact svg { width: 18px; height: 18px; margin-top: 5px; flex: none; }
  .specialty { margin-top: 20px; font-family: "Oswald", sans-serif; font-weight: 500; font-size: 36px; line-height: 40px; text-transform: uppercase; }
  .specialty small { font-size: 20px; }
  .services { margin-top: 8px; font-family: "Roboto Condensed", sans-serif; font-weight: 700; font-size: 19px; line-height: 21px; }
  .hours { margin-top: 8px; font-family: "Oswald", sans-serif; font-size: 17px; line-height: 22px; }
  .offer { position: absolute; left: 0; top: 790px; width: 100%; height: 350px; background: var(--red); color: var(--white); padding: 26px 30px 0 40px; }
  .offer-lead { font-family: "Oswald", sans-serif; font-weight: 500; font-size: 34px; line-height: 42px; text-transform: uppercase; }
  .deal { display: flex; align-items: flex-end; margin-top: 6px; white-space: nowrap; }
  .deal-number { font-family: "Anton", sans-serif; font-size: 150px; line-height: 170px; }
  .deal-words { font-family: "Anton", sans-serif; font-size: 52px; line-height: 60px; margin-left: 14px; padding-bottom: 22px; text-transform: uppercase; }
</style>
</head>
<body>
<article class="flyer">
  <header class="hero">
    <div class="hero-photo" role="img" aria-label="High-contrast photo of a mechanic working under a car on a lift"></div>
    <h1 class="brand">VERLIN<br>AUTO<br>REPAIR</h1>
  </header>
  <section class="details">
    <ul class="contact">
      <li><svg viewBox="0 0 20 20"><circle cx="10" cy="10" r="8" fill="var(--ink)"/><circle cx="10" cy="10" r="3" fill="var(--paper)"/></svg><span>4120 S Harbor Ave.<br>Chicago IL. 60619</span></li>
      <li><svg viewBox="0 0 20 20"><circle cx="10" cy="10" r="9" fill="var(--ink)"/><path d="M7 5l2 3-1 1 3 3 1-1 3 2-1 2c-4 0-8-4-8-8z" fill="var(--paper)"/></svg><span>(773) 555-0148</span></li>
      <li><svg viewBox="0 0 20 20"><circle cx="10" cy="10" r="9" fill="var(--ink)"/><text x="10" y="14" font-size="11" text-anchor="middle" fill="var(--paper)" font-family="sans-serif">@</text></svg><span>VerlinAutoRepair@mailbox.com</span></li>
    </ul>
    <h2 class="specialty">Specializing in<br>Foreign <small>&amp;</small> Domestic Cars</h2>
    <p class="services">Offer includes but is not limited to: brakes, engine/transmission change, electrical work, emission test, oil change and automobile diagnostic ...</p>
    <p class="hours">Hours: Mon.-Fri. 8am-5pm; Sat. 8am-4pm; Sun. Closed</p>
  </section>
  <section class="offer">
    <p class="offer-lead">Bring in your estimate from our competitors with this flyer and you will get</p>
    <div class="deal">
      <span class="deal-number">10%</span>
      <span class="deal-words">Discount<br>on it !!!</span>
    </div>
  </section>
</article>
</body>
</html>
```